Flyer Vermietung von Partyanlagen
Zielgruppe
Wir sind ein junges Unternehmen, welches Veranstaltungsequipment für private Endkunden zur Miete anbietet. Vor allem sind wir auf die Vermietung von 'Komplettpaketen' spezialisiert, die aus Licht- und Audioequipment für eigene Feierlichkeiten bestehen.
Aufgabenstellung
Wir benötigen ein auffälliges und modernes Design, was gerne mit Designelementen geschmückt werden darf. Im Vordergrund muss unser Angebot stehen ( Vermietung professioneller Partyanlagen zu günstigen Preisen). Die Maße können innerhalb der DIN-Vorgaben frei gewählt werden ( DIN- A5/A6/Lang).
Der Leser des Flyers soll angeregt werden, sich für seine Feierlichkeit eine Komplettanlage von uns zu mieten, da diese professionell, günstig und einfach im Aufbau sind.
Ein Beispiel der am häufigsten vermieteten Anlage, sowie unsere Leistungen finden Sie im folgenden Text, der von Ihnen verwendet werden sollte, gerne angepasst werden darf und soll zu Ihrer Information dient.
Unser Angebot :
Party Komplettpaket aus Licht & Ton für deine Party.
Bestehend aus :
2x Tonfels Audio Aktiv Lautsprecher ( 1000 Watt Class D)
1x 15' Subwoofer (1200 Watt Class D)
1x Lichtanlage mit 4 Scheinwerfern
1x raumfüllender LED-Effekt
Mischpult zum Anschluss von Audioquellen ( Laptop o.Ä.)
RBQ Funkmikrofon
Nebelmaschine
- alle nötigen Stative & Kabel
für nur 90 Euro komplett
inklusive Lieferung in Werne ( geringe Aufpreis in der Umgebung)
zu ergänzen zum Beispiel mit :
- Subwoofern
- Movingheads, weiteren Lichteffekten etc.
- Equipmentverleih
- Individuelle Mietanlagen
- Licht-/Tontechnik
- Traversensysteme
- Technischer Support
- Anlieferung & Aufbau
- Dry Hire
Weitere Angaben, die auf dem Flyer erscheinen sollen:
Website : www.7k-eventwerk.de
(Private Daten würden wir später weitergeben)
Unser Logo wird in einem anderen Projekt ausgeschrieben - dafür bitte etwas Platz lassen ( bzw. von dem selben Designer kann es auch nicht schaden ;-) )
Die weiteren Bilder sind leider qualitativ nicht sehr hochwertig ( da jeweils von Kunden) - können aber verwendet werden und dienen ebenfalls Ihrer Veranschaulich..

```html
<!DOCTYPE html>
<html lang="de">
<head>
<meta charset="utf-8">
<title>Flyer – Vermietung von Partyanlagen</title>
<link rel="stylesheet" href="https://fonts.googleapis.com/css2?family=Lobster&family=Open+Sans:wght@400;700;800&display=swap">
<style>
  :root {
    --page-bg: #bdbdbd;
    --flyer-black: #050505;
    --stage-dark: #2a2a2a;
    --stage-mid: #4a4a4a;
    --band-grey: #a9a9ad;
    --script-orange: #e39a17;
    --accent-orange: #e8a018;
    --text-white: #ffffff;
    --text-dark: #151515;
    --footer-white: #ffffff;
  }
  * { box-sizing: border-box; margin: 0; padding: 0; }
  html, body {
    width: 1200px; height: 839px; overflow: hidden;
    background: radial-gradient(ellipse at 60% 40%, #d8d8d8 0%, var(--page-bg) 70%, #9a9a9a 100%);
    font-family: "Open Sans", Arial, sans-serif;
  }
  .flyer {
    position: absolute; left: 317px; top: 20px;
    width: 566px; height: 800px;
    background: var(--flyer-black);
    overflow: hidden;
    box-shadow: 0 6px 24px rgba(0,0,0,.35);
  }
  .stage-photo {
    position: absolute; left: 0; top: 0; width: 566px; height: 430px;
    background:
      radial-gradient(ellipse at 50% 20%, #6b6b6b 0%, transparent 55%),
      linear-gradient(180deg, var(--stage-mid) 0%, var(--stage-dark) 55%, var(--flyer-black) 100%);
  }
  .band-top {
    position: absolute; left: 0; top: 26px; width: 566px; height: 7px;
    background: var(--band-grey);
  }
  .headline-panel {
    position: absolute; left: 0; top: 33px; width: 566px; height: 160px;
    background: rgba(20,20,20,.55);
  }
  .band-bottom {
    position: absolute; left: 0; top: 193px; width: 566px; height: 6px;
    background: var(--band-grey);
  }
  .headline {
    position: absolute; left: 28px; top: 46px;
    font-family: "Lobster", cursive; font-weight: 400;
    color: var(--script-orange); line-height: 1.05;
  }
  .headline .lead { color: var(--text-white); font-size: 32px; }
  .headline .line1 { font-size: 46px; }
  .headline .line2 { display: block; font-size: 48px; }
  .subline {
    position: absolute; left: 30px; top: 155px;
    font-weight: 700; font-size: 21px; line-height: 1.2; color: var(--text-white);
    white-space: nowrap;
  }
  .gallery {
    position: absolute; left: 0; top: 232px; width: 566px; height: 160px;
  }
  .gallery .shot {
    position: absolute; top: 0; width: 140px; height: 140px; border-radius: 50%;
    border: 3px solid #f4f4f4;
    box-shadow: 0 0 14px 4px rgba(255,255,255,.55);
  }
  .shot.setup { left: 42px; top: 16px; background: radial-gradient(circle at 40% 35%, #e9b6ef 0%, #b67ad6 45%, #43305c 100%); }
  .shot.crowd { left: 213px; background: radial-gradient(circle at 50% 30%, #ff2c59 0%, #b0102f 50%, #2a0710 100%); }
  .shot.hall  { left: 384px; top: -14px; background: radial-gradient(circle at 50% 55%, #c69ae6 0%, #7e58b4 45%, #2d2640 100%); }
  .offer-rule {
    position: absolute; left: 52px; top: 418px; width: 122px; height: 3px; background: var(--text-white);
  }
  .offer {
    position: absolute; left: 52px; top: 424px; width: 250px; color: var(--text-white);
  }
  .offer h2 { font-size: 17px; font-weight: 800; line-height: 1.3; }
  .offer .intro { font-size: 10.5px; font-weight: 700; line-height: 1.3; margin-bottom: 18px; }
  .list-title { font-size: 10.5px; font-weight: 700; line-height: 1.5; }
  .item-list { list-style: none; font-size: 10.5px; font-weight: 700; line-height: 1.5; }
  .item-list li::before { content: "– "; }
  .item-list li.wrap { padding-left: 10px; text-indent: -10px; }
  .extras {
    position: absolute; left: 318px; top: 468px; width: 240px; color: var(--text-white);
  }
  .extras .list-title { margin-bottom: 18px; }
  .price {
    position: absolute; left: 60px; top: 660px;
    font-size: 10.5px; font-weight: 700; color: var(--text-white);
  }
  .footer-rule {
    position: absolute; left: 0; top: 690px; width: 566px; height: 5px; background: var(--accent-orange);
  }
  .footer {
    position: absolute; left: 0; top: 695px; width: 566px; height: 105px;
    background: var(--footer-white); color: var(--text-dark);
  }
  .contact {
    position: absolute; left: 34px; top: 14px; font-size: 12.5px; line-height: 1.6;
  }
  .contact strong { font-weight: 700; font-size: 15px; }
  .greeting {
    position: absolute; right: 30px; top: 64px; font-size: 19px;
  }
</style>
</head>
<body>
  <main class="flyer">
    <div class="stage-photo" role="img" aria-label="Dunkles Foto einer Bühne mit Lautsprechern und Nebel"></div>
    <div class="band-top"></div>
    <div class="headline-panel"></div>
    <div class="band-bottom"></div>

    <h1 class="headline">
      <span class="lead">Dein </span><span class="line1">Party- und</span>
      <span class="line2">Veranstaltungsequipment</span>
    </h1>
    <p class="subline">Vermietung professioneller Ton-/Lichtanlagen</p>

    <div class="gallery">
      <div class="shot setup" role="img" aria-label="Foto: Partyanlage mit Lautsprechern auf Stativen und Lichttraverse"></div>
      <div class="shot crowd" role="img" aria-label="Foto: feiernde Gäste in rotem Bühnenlicht"></div>
      <div class="shot hall" role="img" aria-label="Foto: Festsaal mit violetter Beleuchtung und Traversen"></div>
    </div>

    <div class="offer-rule"></div>
    <section class="offer">
      <h2>Unser Angebot :</h2>
      <p class="intro">Party Komplettpaket aus<br>Licht &amp; Ton für deine Party.</p>
      <p class="list-title">Bestehend aus :</p>
      <ul class="item-list">
        <li>2x Tonfels Audio Aktiv Lautsprecher</li>
        <li>1x Lichtanlage mit 4 Scheinwerfern</li>
        <li>1x raumfüllender LED-Effekt</li>
        <li class="wrap">Mischpult zum Anschluss von<br>Audioquellen ( Laptop o. Ä.)</li>
        <li>Funkmikrofon</li>
        <li>Nebelmaschine</li>
      </ul>
    </section>

    <section class="extras">
      <p class="list-title">Zu ergänzen zum Beispiel mit :</p>
      <ul class="item-list">
        <li>Subwoofern</li>
        <li>Movingheads, weiteren Lichteffekten etc.</li>
        <li>Equipmentverleih</li>
        <li>Individuelle Mietanlagen</li>
        <li>Licht-/Tontechnik</li>
        <li>Traversensysteme</li>
        <li>Technischer Support</li>
        <li>Anlieferung &amp; Aufbau</li>
        <li>Dry Hire</li>
      </ul>
    </section>

    <p class="price">Alles ab 90 Euro inklusive Lieferung in Werne und Umgebung!</p>

    <div class="footer-rule"></div>
    <footer class="footer">
      <p class="contact">Besuch uns unter <strong>www.7k-eventwerk.de</strong> oder schreib uns eine<br>unverbindliche Angebotsanfrage an <strong>info@7k-eventwerk.de.</strong></p>
      <p class="greeting">Wir freuen uns auf Dich!</p>
    </footer>
  </main>
</body>
</html>
```